Amber Ridge Publishing Web Page Design

Design a website for my new start up publishing company - Amber Ridge Publishing, the first work published by ARP with be a new book by M.R. Theodor called Silent Ledger. The prototype for the book cover is attached.

Target Market(s)

Worldwide, all readers of mystery, fiction, etc.

Industry/Entity Type

Book Publisher

Coding

Coded - Design and coding required

Number of Pages Required

1 page

```html
<!DOCTYPE html>
<html lang="en">
<head>
<meta charset="utf-8">
<title>Amber Ridge Publishing</title>
<link href="https://fonts.googleapis.com/css2?family=Raleway:wght@300;400;500;600&family=Open+Sans:wght@400;600;700&display=swap" rel="stylesheet">
<style>
:root{
  --yellow:#f7c600;
  --yellow-dark:#e0b000;
  --ink:#222;
  --text:#555;
  --muted:#888;
  --line:#e3e3e3;
  --soft:#f4f4f4;
  --dark:#1c1c1c;
  --darker:#121212;
  --red:#d8232a;
  --social:#2a7fc1;
}
*{box-sizing:border-box;margin:0;padding:0}
html,body{width:1200px;height:4000px;overflow:hidden}
body{font-family:"Open Sans",Arial,sans-serif;color:var(--text);background:#fff;font-size:14px;line-height:1.6}
h1,h2,h3,h4{font-family:"Raleway",Helvetica,sans-serif;color:var(--ink);font-weight:400}
.section-title{text-align:center;font-size:38px;font-weight:300;color:#333}
.section-sub{text-align:center;font-size:12px;color:var(--muted);margin-top:2px}
.btn{display:inline-block;background:var(--yellow);color:#222;font-size:13px;font-weight:600;padding:10px 30px;border-radius:2px}
.underline{display:block;width:50px;height:3px;background:var(--yellow);margin-top:10px}

/* hero */
.hero{position:relative;height:640px;background:linear-gradient(120deg,#3a2f26 0%,#1e1915 45%,#2c241d 100%)}
.hero-shelves{position:absolute;inset:0;background:linear-gradient(180deg,rgba(90,60,35,.45),rgba(20,15,12,.7))}
.nav{position:absolute;top:0;left:0;right:0;height:74px;display:flex;align-items:center;padding:0 80px;background:rgba(0,0,0,.35);z-index:2}
.brand{display:flex;align-items:center;gap:10px}
.brand-mark{width:14px;height:14px;background:var(--yellow);border-radius:50%}
.brand-name{font-family:"Raleway",sans-serif;font-weight:600;color:var(--yellow);font-size:22px;letter-spacing:1px}
.brand-full{font-family:"Raleway",sans-serif;font-weight:600;color:var(--yellow);font-size:12px;line-height:1.2;width:110px}
.menu{display:flex;gap:38px;margin-left:auto;margin-right:40px;list-style:none}
.menu li{color:#fff;font-size:13px;white-space:nowrap}
.menu li.active{color:var(--yellow)}
.social{display:flex;gap:6px}
.social span{width:22px;height:22px;border-radius:50%;background:var(--social)}
.badge{position:absolute;left:115px;top:255px;width:120px;height:120px;border-radius:50%;background:var(--red);color:#fff;font-family:"Raleway",sans-serif;font-weight:600;font-size:17px;text-align:center;display:flex;align-items:center;justify-content:center;line-height:1.2;box-shadow:0 0 0 6px rgba(216,35,42,.35)}
.hero-copy{position:absolute;left:260px;top:250px;width:440px}
.hero-copy h1{color:var(--yellow);font-size:44px;font-weight:400}
.hero-copy p{color:#fff;font-size:21px;line-height:1.3;margin:6px 0 22px}
.hero-dots{position:absolute;left:400px;top:470px;display:flex;gap:8px}
.hero-dots span{width:8px;height:8px;border-radius:50%;background:#aaa}
.hero-dots span:first-child{background:#fff}
.book-cover{position:absolute;left:770px;top:100px;width:300px;height:490px;background:linear-gradient(160deg,#2f3c4c,#16202b 60%,#0c1117);box-shadow:14px 14px 30px rgba(0,0,0,.6);border-left:10px solid #0a0f14}
.book-cover .cover-title{position:absolute;top:28px;left:0;right:0;text-align:center;font-family:"Raleway",sans-serif;font-weight:600;color:var(--yellow);font-size:46px;line-height:1}
.book-cover .cover-author{position:absolute;bottom:28px;left:0;right:0;text-align:center;font-family:"Raleway",sans-serif;font-weight:600;color:#d9d9d9;font-size:24px}

/* stats */
.stats{height:270px;padding-top:40px}
.stat-row{display:flex;justify-content:space-between;width:1000px;margin:45px auto 0}
.stat{display:flex;align-items:center;gap:16px;width:220px}
.stat-icon{width:74px;height:74px;border-radius:50%;background:var(--yellow);display:flex;align-items:center;justify-content:center}
.stat-label{font-size:15px;color:#333}
.stat-num{font-size:16px;color:#333}

/* description */
.description{height:340px;display:flex;gap:40px;padding:0 80px;align-items:center}
.photo{border-radius:2px}
.description .photo{width:500px;height:280px;background:linear-gradient(135deg,#d8d0c4,#8a7562 60%,#5a4a3c)}
.desc-body{width:500px}
.kicker{font-size:13px;color:#444}
.desc-body h2{font-size:34px;font-weight:300}
.desc-body p{font-size:13px;margin-top:14px;color:var(--muted)}

/* books */
.books{position:relative;height:560px;padding-top:30px}
.book-row{display:flex;gap:28px;width:1080px;margin:30px auto 0}
.book-card{width:252px}
.book-card .photo{height:300px}
.b1{background:linear-gradient(160deg,#f1ebe0,#c0432b)}
.b2{background:linear-gradient(160deg,#ece4d6,#b9312b)}
.b3{background:linear-gradient(160deg,#f2eee6,#1f1f1f)}
.b4{background:linear-gradient(160deg,#f5f2ea,#c72a25)}
.book-date{font-size:12px;color:var(--muted);margin-top:12px}
.book-card h3{font-size:20px;margin-top:2px}
.book-card p{font-size:13px;color:var(--muted);line-height:1.4}
.arrow{position:absolute;top:300px;width:24px;height:24px;border-radius:50%;border:1px solid #bbb;display:flex;align-items:center;justify-content:center}
.arrow.left{left:20px}.arrow.right{right:20px}

/* feedback */
.feedback{height:470px;padding-top:10px}
.quote-row{display:flex;gap:30px;width:1000px;margin:34px auto 0}
.quote{position:relative;width:313px;height:280px;border:1px solid var(--line);text-align:center;padding:95px 26px 0}
.quote-mark{position:absolute;left:20px;top:-1px;width:30px;height:30px;background:var(--yellow);color:#222;font-weight:700;font-size:20px;line-height:34px}
.avatar{position:absolute;left:50%;top:18px;margin-left:-37px;width:74px;height:74px;border-radius:50%;background:linear-gradient(135deg,#c9c3bd,#6d665f)}
.quote p{font-size:12px;color:var(--muted);line-height:1.5}
.quote h4{font-size:20px;margin-top:14px}
.role{font-size:11px;color:var(--muted)}
.stars{color:var(--yellow);font-size:13px;letter-spacing:2px}
.dots{display:flex;gap:8px;justify-content:center;margin-top:24px}
.dots span{width:8px;height:8px;border-radius:50%;background:#ccc}
.dots span:first-child{background:#666}

/* author */
.author{height:390px;display:flex;gap:60px;padding:0 80px;align-items:center}
.author-body{width:520px}
.author-body h2{font-size:40px;font-weight:300}
.author-body p{font-size:13px;color:var(--muted);margin-top:14px}
.author .photo{width:500px;height:300px;background:linear-gradient(135deg,#4b4f55,#1f2226 60%,#bfb8ad)}

/* news */
.news{height:510px;padding-top:20px;text-align:center}
.news-row{display:flex;gap:36px;width:1000px;margin:34px auto 30px;text-align:left}
.news-card{width:310px;border:1px solid var(--line)}
.news-card .photo{height:180px;border-radius:0}
.n1{background:linear-gradient(135deg,#6a4a30,#2a1d14)}
.n2{background:linear-gradient(135deg,#c9c3b8,#5a3a28)}
.n3{background:linear-gradient(135deg,#e9e1d6,#7a5a48)}
.news-date{display:block;width:120px;margin:-14px auto 0;position:relative;background:var(--yellow);font-size:12px;text-align:center;padding:4px 0;color:#222}
.news-body{padding:10px 14px 14px}
.news-body h3{font-size:17px}
.news-body p{font-size:12px;color:var(--muted);line-height:1.45}
.read{font-size:12px;color:#333;text-decoration:underline}

/* contact */
.contact{height:410px;padding-top:10px;text-align:center}
.form{width:760px;margin:34px auto 0;text-align:left}
.field-row{display:flex;gap:20px}
.field{flex:1;background:var(--soft);height:44px;padding:12px 14px;font-size:13px;color:var(--muted)}
.field.message{height:150px;margin-top:16px}
.form .btn{display:block;width:130px;margin:22px auto 0;text-align:center}

/* footer */
.footer{height:360px;background:var(--dark);display:flex;gap:70px;padding:60px 80px 0}
.footer h4{color:#fff;font-size:17px;margin-bottom:14px}
.footer p,.footer li{color:#bbb;font-size:13px;list-style:none;line-height:1.9}
.footer-brand{width:270px}
.footer-brand .brand{margin-bottom:14px}
.contact-line{display:flex;gap:10px;align-items:flex-start}
.contact-line svg{flex:none;margin-top:6px}
.subscribe-input{background:#fff;height:34px;width:230px;font-size:12px;color:var(--muted);padding:8px 10px;margin-top:6px}
.subscribe-btn{background:var(--yellow);height:34px;width:230px;text-align:center;font-size:13px;font-weight:600;color:#222;padding-top:7px;margin-top:8px}
.copyright{height:50px;background:var(--darker);display:flex;align-items:center;justify-content:space-between;padding:0 80px;color:#999;font-size:12px}
</style>
</head>
<body>

<header class="hero">
  <div class="hero-shelves" role="img" aria-label="Dim library bookshelves background"></div>
  <nav class="nav">
    <div class="brand"><span class="brand-mark"></span><span class="brand-name">ARP</span><span class="brand-full">Amber Ridge Publishing</span></div>
    <ul class="menu">
      <li class="active">Home</li><li>Books</li><li>Authors</li><li>About us</li><li>Latest News</li><li>Contactus</li>
    </ul>
    <div class="social"><span></span><span></span><span></span><span></span></div>
  </nav>
  <div class="badge">NEW<br>RELEASE</div>
  <div class="hero-copy">
    <h1>Silent Ledger</h1>
    <p>Murder, Conspiracy, Change Orders The Construction Business Can be a Killer</p>
    <span class="btn">Read More</span>
  </div>
  <div class="hero-dots"><span></span><span></span><span></span><span></span></div>
  <div class="book-cover" role="img" aria-label="Silent Ledger book cover with stormy city artwork">
    <div class="cover-title">SILENT<br>LEDGER</div>
    <div class="cover-author">M.R. THEODOR</div>
  </div>
</header>

<section class="stats">
  <h2 class="section-title">Over The Year This Book</h2>
  <div class="stat-row">
    <div class="stat"><div class="stat-icon"><svg width="30" height="30" viewBox="0 0 30 30"><rect x="6" y="4" width="18" height="22" fill="none" stroke="#fff" stroke-width="2"/><line x1="10" y1="11" x2="20" y2="11" stroke="#fff" stroke-width="2"/><line x1="10" y1="16" x2="20" y2="16" stroke="#fff" stroke-width="2"/></svg></div><div><div class="stat-label">Topics</div><div class="stat-num">95</div></div></div>
    <div class="stat"><div class="stat-icon"><svg width="30" height="30" viewBox="0 0 30 30"><path d="M5 8h20v16H5z M5 8l10 8 10-8" fill="none" stroke="#fff" stroke-width="2"/></svg></div><div><div class="stat-label">Copies Sold</div><div class="stat-num">15,000</div></div></div>
    <div class="stat"><div class="stat-icon"><svg width="30" height="30" viewBox="0 0 30 30"><path d="M4 6h9c1 0 2 1 2 2v16c0-1-1-2-2-2H4z M26 6h-9c-1 0-2 1-2 2v16c0-1 1-2 2-2h9z" fill="none" stroke="#fff" stroke-width="2"/></svg></div><div><div class="stat-label">Copies Released</div><div class="stat-num">20,000</div></div></div>
    <div class="stat"><div class="stat-icon"><svg width="30" height="30" viewBox="0 0 30 30"><circle cx="15" cy="15" r="10" fill="none" stroke="#fff" stroke-width="2"/><path d="M10 17c2 3 8 3 10 0" fill="none" stroke="#fff" stroke-width="2"/></svg></div><div><div class="stat-label">Happy Reader</div><div class="stat-num">1490</div></div></div>
  </div>
</section>

<section class="description">
  <div class="photo" role="img" aria-label="Person reading an open book"></div>
  <div class="desc-body">
    <div class="kicker">Know More About Book</div>
    <h2>Short Description</h2>
    <span class="underline"></span>
    <p>Lorem Ipsum is simply dummy text of the printing and typesetting industry. Lorem Ipsum has been the industry's standard dummy text ever since.</p>
    <p>When an unknown printer took a galley of type and scrambled it to make a type specimen book. It has survived not only five centuries, but also the leap into electronic typesetting, remaining essentially unchanged.</p>
    <p>It was popularised in the 1960s with the release of Letraset sheets containing Lorem Ipsum passages.</p>
  </div>
</section>

<section class="books">
  <h2 class="section-title">Our Other Books</h2>
  <div class="arrow left"><svg width="10" height="10" viewBox="0 0 10 10"><path d="M7 1L3 5l4 4" fill="none" stroke="#888" stroke-width="1.5"/></svg></div>
  <div class="arrow right"><svg width="10" height="10" viewBox="0 0 10 10"><path d="M3 1l4 4-4 4" fill="none" stroke="#888" stroke-width="1.5"/></svg></div>
  <div class="book-row">
    <article class="book-card"><div class="photo b1" role="img" aria-label="Book cover with red triangular pattern"></div><div class="book-date">July 21, 2018</div><h3>Book Title Here</h3><p>Lorem Ipsum is simply dummy a text of the printing and typesetting industry.</p></article>
    <article class="book-card"><div class="photo b2" role="img" aria-label="Book cover with red triangle on cream"></div><div class="book-date">June 21, 2018</div><h3>Book Title Here</h3><p>Lorem Ipsum is simply dummy a text of the printing and typesetting industry.</p></article>
    <article class="book-card"><div class="photo b3" role="img" aria-label="Book cover with bold black title lettering"></div><div class="book-date">July 21, 2017</div><h3>Book Title Here</h3><p>Lorem Ipsum is simply dummy a text of the printing and typesetting industry.</p></article>
    <article class="book-card"><div class="photo b4" role="img" aria-label="Book cover with large black and red type"></div><div class="book-date">June 21, 2018</div><h3>Book Title Here</h3><p>Lorem Ipsum is simply dummy a text of the printing and typesetting industry.</p></article>
  </div>
</section>

<section class="feedback">
  <h2 class="section-title">Reader's Feedback</h2>
  <p class="section-sub">It's Positive &amp; Great</p>
  <div class="quote-row">
    <article class="quote"><span class="quote-mark">&ldquo;</span><div class="avatar" role="img" aria-label="Reader portrait"></div><p>Lorem Ipsum has been the industry's and standard dummy text ever since the type unknown printer took a galley.</p><h4>Samantha Reyes</h4><div class="role">Creative Director</div><div class="stars">★★★★★</div></article>
    <article class="quote"><span class="quote-mark">&ldquo;</span><div class="avatar" role="img" aria-label="Reader portrait"></div><p>Lorem Ipsum has been the industry's and standard dummy text ever since the type unknown printer took a galley.</p><h4>Austin Barlow</h4><div class="role">Creative Director</div><div class="stars">★★★★★</div></article>
    <article class="quote"><span class="quote-mark">&ldquo;</span><div class="avatar" role="img" aria-label="Reader portrait"></div><p>Lorem Ipsum has been the industry's and standard dummy text ever since the type unknown printer took a galley.</p><h4>Hayden Calloway</h4><div class="role">Creative Director</div><div class="stars">★★★★★</div></article>
  </div>
  <div class="dots"><span></span><span></span><span></span></div>
</section>

<section class="author">
  <div class="author-body">
    <div class="kicker">About us</div>
    <h2>Meet The Author</h2>
    <span class="underline"></span>
    <p>Lorem Ipsum is simply dummy text of the printing and typesetting industry. Lorem Ipsum has been the industry's standard dummy text ever since.</p>
    <p>When an unknown printer took a galley of type and scrambled it to make a type specimen book. It has survived not only five centuries, but also the leap into electronic typesetting, remaining essentially unchanged.</p>
    <p>It was popularised in the 1960s with the release of Letraset sheets containing Lorem Ipsum passages.</p>
  </div>
  <div class="photo" role="img" aria-label="Author writing at a desk with a laptop"></div>
</section>

<section class="news">
  <h2 class="section-title">Latest News</h2>
  <div class="news-row">
    <article class="news-card"><div class="photo n1" role="img" aria-label="Library shelves"></div><span class="news-date">July 26, 2018</span><div class="news-body"><h3>News Title Heading here 01</h3><p>Lorem Ipsum is simply dummy text of the printing and typesetting industry. Lorem Ipsum has been.</p><span class="read">Read More</span></div></article>
    <article class="news-card"><div class="photo n2" role="img" aria-label="Stack of books with a coffee cup"></div><span class="news-date">July 26, 2018</span><div class="news-body"><h3>News Title Heading here 02</h3><p>Lorem Ipsum is simply dummy text of the printing and typesetting industry. Lorem Ipsum has been.</p><span class="read">Read More</span></div></article>
    <article class="news-card"><div class="photo n3" role="img" aria-label="Open book with pages fanned"></div><span class="news-date">July 26, 2018</span><div class="news-body"><h3>News Title Heading here 03</h3><p>Lorem Ipsum is simply dummy text of the printing and typesetting industry. Lorem Ipsum has been.</p><span class="read">Read More</span></div></article>
  </div>
  <span class="btn">View More</span>
</section>

<section class="contact">
  <h2 class="section-title">Quick Contact</h2>
  <div class="form">
    <div class="field-row"><div class="field">Name</div><div class="field">Email</div><div class="field">Phone</div></div>
    <div class="field message">Message</div>
    <span class="btn">Send Now</span>
  </div>
</section>

<footer class="footer">
  <div class="footer-brand">
    <div class="brand"><span class="brand-mark"></span><span class="brand-name">ARP</span><span class="brand-full">Amber Ridge Publishing</span></div>
    <p>Lorem Ipsum is simply dummy text of the printing and typesetting industry.</p>
    <p>Read More &rsaquo;</p>
  </div>
  <div>
    <h4>Quick Link</h4>
    <ul><li>&bull; Home</li><li>&bull; Books</li><li>&bull; Authors</li><li>&bull; About us</li><li>&bull; Blogs</li><li>&bull; Contactus</li></ul>
  </div>
  <div>
    <h4>Quick Contact</h4>
    <div class="contact-line"><svg width="12" height="14" viewBox="0 0 12 14"><path d="M6 13S1 8 1 5a5 5 0 0110 0c0 3-5 8-5 8z" fill="var(--yellow)"/></svg><p>48 Orchard Lane<br>Millbrook, USA<br>Zip: 10245</p></div>
    <div class="contact-line"><svg width="12" height="12" viewBox="0 0 12 12"><path d="M2 1h3l1 3-2 1a7 7 0 003 3l1-2 3 1v3c-6 0-9-3-9-9z" fill="var(--yellow)"/></svg><p>+100 555 0134</p></div>
    <div class="contact-line"><svg width="12" height="10" viewBox="0 0 12 10"><rect x="0.5" y="0.5" width="11" height="9" fill="none" stroke="var(--yellow)"/><path d="M1 1l5 4 5-4" fill="none" stroke="var(--yellow)"/></svg><p>info@amberridgepub.com</p></div>
  </div>
  <div>
    <h4>Subscribe</h4>
    <p>Subscribe For Our Newsletter</p>
    <div class="subscribe-input">Email Address</div>
    <div class="subscribe-btn">Subscribe</div>
  </div>
</footer>
<div class="copyright">
  <span>Copyright &copy; 2018 Amber Ridge Publishing. All Right Reserve.</span>
  <div class="social"><span></span><span></span><span></span><span></span></div>
</div>

</body>
</html>
```